Sign Front of Business

Sign for front of workshop. We want KRT Mechanical in same font and colour as logo then the logo after name. Would like a background colour maybe dark blue with a border.

Target Market(s)

Mining Community

Industry/Entity Type

Mechanical

Requirements
Must have
• Logo colours

```html
<!DOCTYPE html>
<html lang="en">
<head>
<meta charset="UTF-8">
<title>KRT Mechanical – Workshop Sign</title>
<link rel="stylesheet" href="https://fonts.googleapis.com/css2?family=Orbitron:wght@700;900&display=swap">
<style>
  :root {
    --page-bg: #d9dbde;
    --navy-deep: #020a4a;
    --navy: #06218f;
    --blue-bright: #0a5fe0;
    --name-blue-top: #3aa0ff;
    --name-blue-bottom: #0a3fc4;
    --silver-light: #ffffff;
    --silver-mid: #c9ccd2;
    --silver-dark: #7d828b;
    --mark-text: #e6e9ee;
    --mark-disc: #0d2f9e;
  }

  html, body {
    margin: 0;
    padding: 0;
    width: 1200px;
    height: 1020px;
    overflow: hidden;
  }

  body {
    background: var(--page-bg);
    display: flex;
    align-items: center;
    justify-content: center;
    font-family: "Orbitron", sans-serif;
  }

  .sign-frame {
    width: 1120px;
    height: 176px;
    padding: 10px;
    box-sizing: border-box;
    background: linear-gradient(90deg,
      var(--silver-dark) 0%, var(--silver-light) 18%, var(--silver-mid) 40%,
      var(--silver-light) 62%, var(--silver-dark) 82%, var(--silver-light) 100%);
    box-shadow: 0 6px 14px rgba(0, 0, 0, 0.35);
  }

  .sign-panel {
    position: relative;
    width: 100%;
    height: 100%;
    overflow: hidden;
    background: linear-gradient(120deg,
      var(--navy-deep) 0%, var(--navy) 35%, var(--blue-bright) 58%,
      var(--navy) 80%, var(--navy-deep) 100%);
    display: flex;
    align-items: center;
  }

  .business-name {
    position: relative;
    margin: 0 0 0 58px;
    font-size: 64px;
    font-weight: 900;
    letter-spacing: 3px;
    white-space: nowrap;
    line-height: 1;
  }

  .business-name .initials {
    background: linear-gradient(180deg, var(--name-blue-top), var(--name-blue-bottom));
    -webkit-background-clip: text;
    background-clip: text;
    color: transparent;
  }

  .business-name .trade {
    margin-left: 18px;
    background: linear-gradient(180deg, var(--silver-light) 0%, var(--silver-mid) 48%, var(--silver-dark) 52%, var(--silver-light) 100%);
    -webkit-background-clip: text;
    background-clip: text;
    color: transparent;
  }

  .brand-mark {
    position: relative;
    margin-left: auto;
    margin-right: 48px;
    display: flex;
    align-items: center;
    gap: 14px;
  }

  .brand-mark .disc {
    width: 70px;
    height: 70px;
    border-radius: 50%;
    background: var(--mark-disc);
    border: 3px solid var(--mark-text);
    box-sizing: border-box;
  }

  .brand-mark .mark-name {
    font-size: 22px;
    font-weight: 900;
    color: var(--mark-text);
    line-height: 1.2;
    letter-spacing: 1px;
  }
</style>
</head>
<body>
  <div class="sign-frame">
    <div class="sign-panel">
      <h1 class="business-name"><span class="initials">KRT</span><span class="trade">MECHANICAL</span></h1>
      <div class="brand-mark">
        <span class="disc"></span>
        <span class="mark-name">KRT<br>MECHANICAL</span>
      </div>
    </div>
  </div>
</body>
</html>
```